Web Design for an Online Dating Web Site

We need an uncoded web design for a new online dating web site called pLirvo.com. Simplicity and boldness are the key factors in the successful design.
Please look at the requirements document attached for details.
Updates
Dear all,
Please AVOID USING A PICTURE OF A HAPPY COUPLE ON THE HOME PAGE of the site. We highly want to move away from this space as it makes our web site just like another dating web site.
We like something simple with web 2.0 look and feel. The examples in the Requirements Document are exactly the design we are after.
Regards
Tarn
Industry/Entity Type
Dating
Look and feel
Each slider illustrates characteristics of the customer's brand and the style your logo design should communicate.

```html
<!DOCTYPE html>
<html lang="en">
<head>
<meta charset="utf-8">
<title>pLirvo.com – Start dating now</title>
<link href="https://fonts.googleapis.com/css2?family=Source+Sans+3:wght@400;700&display=swap" rel="stylesheet">
<style>
:root{
  --pink:#ee5b9d;
  --ink:#444;
  --ink-strong:#555;
  --bar:#2b2828;
  --bar-light:#3a3636;
  --field:#bdbdbe;
  --field-top:#f2f2f2;
  --rule:#cfcfcf;
  --white:#fff;
  --blue:#1f6fb5;
  --orange:#ef7d22;
  --silver:#d6d6d6;
  --sky:#8ccbe6;
}
*{box-sizing:border-box;margin:0;padding:0}
html,body{width:1200px;height:800px;overflow:hidden}
body{font-family:"Source Sans 3",Arial,sans-serif;color:var(--ink);position:relative;
  background:linear-gradient(#dcdcdc 0,#fafafa 130px,#fff 400px,#fff 660px,#e2e2e2 760px)}
.abs{position:absolute}

/* header */
.site-header{position:absolute;left:0;top:0;width:1200px;height:100px;
  background:radial-gradient(ellipse at 55% 30%,var(--bar-light),var(--bar) 70%)}
.brand{left:100px;top:6px;font-size:64px;font-weight:700;color:var(--pink);line-height:1;letter-spacing:-1px}
.brand-url{left:272px;top:61px;font-size:12px;color:#bbb}
.login label{position:absolute;font-size:12px;color:#ccc}
.login .input{position:absolute;width:150px;height:20px;border-radius:4px;background:linear-gradient(var(--field-top),#fff)}
.login .btn{position:absolute;left:894px;top:28px;width:61px;height:21px;border-radius:4px;background:linear-gradient(#fff,#ddd);
  font-size:12px;font-weight:700;color:#222;text-align:center;line-height:21px}
.login .small{position:absolute;font-size:10px;color:#aaa}
.check{position:absolute;left:568px;top:56px;width:11px;height:11px;background:#fff;border-radius:2px}
.header-icons{left:990px;top:30px}

/* content */
.divider{left:600px;top:120px;width:1px;height:560px;background:var(--rule)}
h1,h2{position:absolute;color:var(--pink);font-weight:700;line-height:1}
.how-title{left:75px;top:205px;font-size:40px}
.how-sub{position:absolute;left:75px;top:248px;font-size:23px;font-weight:700;color:var(--ink-strong);line-height:28px}
.how-text{position:absolute;left:75px;top:282px;width:500px;font-size:16px;line-height:20.5px;color:#333;white-space:nowrap}
.slide{left:100px;top:365px;width:420px;height:290px;border-radius:6px;
  background:radial-gradient(ellipse at 50% 50%,#f4c3cf 0,#e9c06a 30%,#9cc4e8 55%,#fff 80%)}
.slide-dots{left:259px;top:658px;display:flex;gap:11px}
.slide-dots span{width:12px;height:12px;border-radius:50%;border:1.5px solid #777;background:#fff}
.slide-dots .on{background:var(--pink);border-color:#999}

.start-title{left:676px;top:204px;font-size:38px}
.rule{position:absolute;left:676px;width:449px;height:1px;background:var(--rule)}
.signup-form .label{position:absolute;right:384px;font-size:21px;color:var(--ink);line-height:30px}
.signup-form .field{position:absolute;left:832px;width:293px;height:30px;border-radius:6px;background:var(--field)}
.signup-btn{left:1048px;top:533px;width:77px;height:25px;border-radius:6px;background:var(--pink);
  color:#fff;font-weight:700;font-size:16px;text-align:center;line-height:25px}
.signup-btn.reflect{top:559px;transform:scaleY(-1);opacity:.22}
.or-title{left:676px;top:578px;font-size:36px}
.social a{position:absolute;width:40px;height:40px;border-radius:7px;color:#fff;font-size:9px;font-weight:700;
  display:flex;align-items:center;justify-content:center;text-decoration:none}
.social .reflect{opacity:.2;height:30px;border-radius:0 0 7px 7px}

/* footer */
.site-footer{position:absolute;left:0;top:760px;width:1200px;height:40px;background:var(--bar);color:var(--white);font-size:15px}
.footer-nav{left:126px;top:11px}
.footer-nav span{margin:0 6px;color:#ccc}
.mini{position:absolute;top:10px;width:20px;height:20px;border-radius:3px}
.copyright{left:926px;top:12px;font-size:14px}
.copyright b{color:var(--pink);font-weight:400}
</style>
</head>
<body>
<header class="site-header">
  <div class="abs brand">pLirvo</div>
  <div class="abs brand-url">pLirvo.com</div>
  <form class="login">
    <label style="left:568px;top:12px">Email</label>
    <div class="input" style="left:568px;top:28px"></div>
    <label style="left:731px;top:12px">Password</label>
    <div class="input" style="left:731px;top:28px"></div>
    <div class="btn">Log in</div>
    <span class="check"></span>
    <span class="small" style="left:587px;top:56px">Keep me logged in</span>
    <span class="small" style="left:731px;top:56px">Forgot your password?</span>
  </form>
  <svg class="abs header-icons" width="115" height="18" viewBox="0 0 115 18" fill="none" stroke="#999" stroke-width="1.3">
    <rect x="1" y="4" width="14" height="11"/><path d="M1 4l7 6 7-6"/>
    <circle cx="39" cy="5" r="4"/><path d="M32 16c0-5 14-5 14 0z"/>
    <rect x="63" y="5" width="15" height="10" rx="1"/><circle cx="70.5" cy="10" r="3"/><path d="M66 5l1-2h4l1 2"/>
    <path d="M95 4c3-1 6-1 8 1v11c-2-2-5-2-8-1zM103 5c2-2 5-2 8-1v11c-3-1-6-1-8 1"/>
  </svg>
</header>

<div class="abs divider"></div>

<section class="how-it-works">
  <h1 class="how-title">How it works ?</h1>
  <p class="how-sub">CLICK FOR BETTER RELATION...</p>
  <p class="how-text">Lorem ipsum dolor sit amet, consectetur adipisicing elit, sed<br>do eiusmod tempor incididunt ut labore et dolore magna aliqua.<br>Ut enim ad minim veniam, quis nostrud exercitation ullamco laboris<br>nisi ut aliquip ex ea...</p>
  <div class="abs slide" role="img" aria-label="Illustration of game pieces linked in a network around a red heart"></div>
  <div class="abs slide-dots"><span></span><span class="on"></span><span></span><span></span></div>
</section>

<section class="signup">
  <h2 class="start-title">Start dating now !</h2>
  <div class="rule" style="top:257px"></div>
  <form class="signup-form">
    <span class="label" style="top:275px">First Name :</span><div class="field" style="top:275px"></div>
    <span class="label" style="top:327px">Last Name :</span><div class="field" style="top:327px"></div>
    <span class="label" style="top:378px">Your Email :</span><div class="field" style="top:378px"></div>
    <span class="label" style="top:430px">Re-enter Email :</span><div class="field" style="top:430px"></div>
    <span class="label" style="top:481px">Password :</span><div class="field" style="top:481px"></div>
  </form>
  <div class="abs signup-btn">Sign Up</div>
  <div class="abs signup-btn reflect" aria-hidden="true">Sign Up</div>
  <h2 class="or-title">Or use...</h2>
  <div class="rule" style="top:626px"></div>
  <nav class="social">
    <a href="#" style="left:898px;top:641px;background:var(--blue)">Friendlo</a>
    <a href="#" style="left:960px;top:641px;background:var(--orange)">Newsrill</a>
    <a href="#" style="left:1022px;top:641px;background:var(--silver);color:#666">Snapbox</a>
    <a href="#" style="left:1085px;top:641px;background:var(--sky)">Chirpr</a>
    <span class="reflect" style="position:absolute;left:898px;top:683px;width:40px;background:linear-gradient(var(--blue),transparent)"></span>
    <span class="reflect" style="position:absolute;left:960px;top:683px;width:40px;background:linear-gradient(var(--orange),transparent)"></span>
    <span class="reflect" style="position:absolute;left:1022px;top:683px;width:40px;background:linear-gradient(var(--silver),transparent)"></span>
    <span class="reflect" style="position:absolute;left:1085px;top:683px;width:40px;background:linear-gradient(var(--sky),transparent)"></span>
  </nav>
</section>

<footer class="site-footer">
  <svg class="abs" style="left:100px;top:11px" width="18" height="16" viewBox="0 0 18 16"><path d="M9 1L1 8h2v7h4v-4h4v4h4V8h2z" fill="var(--pink)"/></svg>
  <div class="abs footer-nav">Why pLirvo<span>|</span>How it works<span>|</span>Sign Up<span>|</span>About Us</div>
  <span class="mini" style="left:767px;background:var(--blue)" aria-label="Friendlo"></span>
  <span class="mini" style="left:798px;background:var(--orange)" aria-label="Newsrill"></span>
  <span class="mini" style="left:830px;background:var(--silver)" aria-label="Snapbox"></span>
  <span class="mini" style="left:861px;background:var(--sky)" aria-label="Chirpr"></span>
  <div class="abs copyright">COPYRIGHT © 2011 <b>PLIRVO.</b></div>
</footer>
</body>
</html>
```